LEARN Business Skills so you can Earn a good living

size of the poster is 8”x 10.75" plus 0.25" bleed.
Please leave 1 inch on the bottoum for footer
I want a design a poster that will attract people's attention.
I appreciate a creative ad however the ad should not take away from being able to clearly read the text.
-I also appreciate a simple creative ad that is not too busy.
-you can use graphics, vectors, or pictures of real people.
-however, if you use real people it should be a white male that is wearing a white shirt and look like a professional person.

Target Market(s)

Potential young business people

Industry/Entity Type

education

Requirements
Must have
• easy to read the text
Nice to have
• I would like a "creative" simple ad that is easy to be read
Should not have
• pictures of women

```html
<!DOCTYPE html>
<html lang="en">
<head>
<meta charset="utf-8">
<title>Learn to Earn – Business Enrichment Course</title>
<link href="https://fonts.googleapis.com/css2?family=League+Spartan:wght@400;500;600;700&display=swap" rel="stylesheet">
<style>
  :root {
    --brand-red: #a62831;
    --accent-red: #b3222e;
    --ink: #0a0a0a;
    --paper: #ffffff;
    --backdrop: #e9eaec;
  }
  * { margin: 0; padding: 0; box-sizing: border-box; }
  html, body {
    width: 1200px; height: 1200px; overflow: hidden;
    background: var(--backdrop);
    font-family: "League Spartan", sans-serif;
  }
  .poster {
    position: absolute; left: 185px; top: 10px;
    width: 830px; height: 1180px;
    background: var(--paper);
    overflow: hidden;
  }
  .hero {
    position: absolute; left: 0; top: 0; width: 100%; height: 760px;
    background: var(--brand-red);
    color: var(--paper);
  }
  .headline-block {
    position: absolute; right: 334px; top: 88px;
    text-align: right; font-weight: 700; line-height: 1; white-space: nowrap;
  }
  .headline-learn {
    display: block; font-size: 132px; letter-spacing: -3px; margin-right: -3px;
  }
  .headline-earn { display: block; margin-top: -14px; }
  .headline-earn .to { font-size: 58px; margin-right: 6px; }
  .headline-earn .earn { font-size: 92px; letter-spacing: -2px; margin-right: -2px; }
  .course-title {
    position: absolute; left: 512px; top: 98px;
    font-size: 39px; font-weight: 700; line-height: 41px; white-space: nowrap;
  }
  .classroom-scene {
    position: absolute; left: 175px; top: 322px;
    width: 475px; height: 366px;
  }
  .tagline {
    position: absolute; left: 0; right: 0; top: 725px;
    text-align: center; font-size: 20px; font-weight: 600; letter-spacing: 0.4px;
  }
  .skills-band {
    position: absolute; left: 0; top: 760px; width: 100%; height: 95px;
    background: var(--ink); color: var(--paper);
  }
  .skills-label {
    position: absolute; left: 130px; top: 10px; width: 250px;
    text-align: right; font-weight: 600;
  }
  .skills-label .small { font-size: 15px; }
  .skills-label .big { font-size: 50px; font-weight: 600; color: var(--accent-red); line-height: 1; }
  .skills-label .line-one { display: flex; align-items: flex-end; justify-content: flex-end; gap: 4px; height: 48px; }
  .skills-label .line-one .small { padding-bottom: 6px; }
  .skills-label .line-two { margin-top: 0; }
  .skills-label .red { color: var(--accent-red); font-size: 21px; font-weight: 500; }
  .benefits {
    position: absolute; left: 395px; top: 14px; list-style: none;
    font-size: 17px; font-weight: 600; line-height: 24px;
  }
  .benefits li::before { content: "•"; color: var(--accent-red); margin-right: 10px; }
  .course-list {
    position: absolute; left: 0; right: 0; top: 882px;
    text-align: center; color: var(--ink);
    font-size: 15.5px; font-weight: 600; line-height: 30.2px;
  }
  .course-list .hl { color: var(--accent-red); }
  .footer-rule {
    position: absolute; left: 0; right: 0; top: 1074px;
    height: 3px; background: var(--accent-red);
  }
</style>
</head>
<body>
  <main class="poster">
    <section class="hero">
      <div class="headline-block">
        <span class="headline-learn">LEARN</span>
        <span class="headline-earn"><span class="to">to</span><span class="earn">EARN</span></span>
      </div>
      <div class="course-title">Business<br>Enrichment<br>Course</div>

      <svg class="classroom-scene" role="img" aria-label="Illustration of a businessman in a suit presenting at a flip chart to two seated students" viewBox="0 0 475 366">
        <defs>
          <linearGradient id="sceneTone" x1="0" y1="0" x2="0" y2="1">
            <stop offset="0" stop-color="#d8cfd0"/>
            <stop offset="0.45" stop-color="#5a1c22"/>
            <stop offset="1" stop-color="#2a0f12"/>
          </linearGradient>
        </defs>
        <rect x="0" y="0" width="475" height="366" rx="6" fill="url(#sceneTone)" opacity="0.55"/>
      </svg>

      <p class="tagline">A PROVEN SUCCESS OF HELPING PEOPLE IN THEIR LIVELIHOODS</p>
    </section>

    <section class="skills-band">
      <div class="skills-label">
        <div class="line-one"><span class="small">BUSINESS</span><span class="big">SKILLS</span></div>
        <div class="line-two"><span class="small">THAT WILL</span> <span class="red">HELP YOU:</span></div>
      </div>
      <ul class="benefits">
        <li>GET A QUALITY JOB</li>
        <li>START/GROW YOUR BUSINESS</li>
        <li>INCREASE YOUR SALARY</li>
      </ul>
    </section>

    <section class="course-list">
      <p>• <span class="hl">BUSINESS ADMIISTRATION</span> • SMALL BUSINESS MANAGEMENT</p>
      <p>• <span class="hl">FINANCE</span> • INVESTMENTS • <span class="hl">COMPUTERS</span> • ACCOUNTING • <span class="hl">SALES MARKETING</span></p>
      <p>• PROJECT MANAGEMENT INTERVIEWING SKILLS • <span class="hl">BUSINESS LAW</span> • NEGOTIATION</p>
      <p>• <span class="hl">PUBLIC SPEAKING</span> • IMPORT/EXPORT • <span class="hl">INFORMATION TECHNOLOY</span></p>
      <p>• DISTRIBUTION • <span class="hl">MARKETING</span> • LEDGERPRO • <span class="hl">REAL ESTATE</span></p>
      <p>• HEALTH CARE • <span class="hl">MANAGEMENT</span> • SHOPFRONT</p>
    </section>

    <div class="footer-rule"></div>
  </main>
</body>
</html>
```